MR Business Card

I want to create a simple business card.
I am a consultant. I design and develop furniture, lighting and accessories for hospitality and retail brands.
I want the card to be simple and clean. Not too much of a logo - but it needs the basic information shown on the attached file.
Also - I have shown some fonts that I like on the attached file.
The card can be square or rectangle. It should be double sided.
I prefer 1-2 colors (not too colorful - but using color an an accent) Even if using color on the edges as an accent.

My snapgrove link shows some other graphics styles that I like. I like clean and simple.
http://www.snapgrove-boards.net/marenrosko/business-cards/

```html
<!DOCTYPE html>
<html lang="en">
<head>
<meta charset="utf-8">
<title>Maren Rosko – Business Card</title>
<link href="https://fonts.googleapis.com/css2?family=Abel&family=Lato:wght@400&display=swap" rel="stylesheet">
<style>
  :root {
    --backdrop: #5b4131;
    --card: #ffffff;
    --ink: #1c1c1c;
    --rule: #2a2a2a;
  }
  * { margin: 0; padding: 0; box-sizing: border-box; }
  html, body {
    width: 1060px;
    height: 1200px;
    overflow: hidden;
    background: var(--backdrop);
  }
  .canvas {
    position: relative;
    width: 1060px;
    height: 1200px;
  }
  .card {
    position: absolute;
    left: 35px;
    width: 977px;
    height: 558px;
    background: var(--card);
    color: var(--ink);
  }
  .card--front { top: 22px; }
  .card--back { top: 605px; }

  /* Front */
  .name {
    position: absolute;
    left: 0;
    right: 0;
    top: 250px;
    text-align: center;
    font-family: "Lato", sans-serif;
    font-weight: 400;
    font-size: 50px;
    letter-spacing: 2px;
    line-height: 1;
  }
  .rule {
    position: absolute;
    height: 2px;
    background: var(--rule);
  }
  .rule--name { left: 250px; width: 476px; top: 309px; }

  /* Back */
  .contact {
    position: absolute;
    left: 78px;
    top: 122px;
    font-family: "Abel", sans-serif;
    font-size: 29px;
    letter-spacing: 3.4px;
    line-height: 38px;
  }
  .tagline {
    position: absolute;
    left: 0;
    right: 0;
    top: 400px;
    text-align: center;
    font-family: "Abel", sans-serif;
    font-size: 35px;
    letter-spacing: 2px;
    line-height: 1;
  }
  .rule--tagline { left: 308px; width: 346px; top: 448px; }
  .services {
    position: absolute;
    left: 0;
    right: 0;
    top: 476px;
    text-align: center;
    font-family: "Abel", sans-serif;
    font-size: 34px;
    letter-spacing: 0.4px;
    word-spacing: 10px;
    line-height: 1;
  }
</style>
</head>
<body>
<main class="canvas">
  <section class="card card--front">
    <h1 class="name">MAREN ROSKO</h1>
    <div class="rule rule--name" aria-hidden="true"></div>
  </section>

  <section class="card card--back">
    <div class="contact">
      <p class="contact__email">maren@marenrosko.com</p>
      <p class="contact__phone">917.555.0148</p>
    </div>
    <p class="tagline">hospitality &amp; home</p>
    <div class="rule rule--tagline" aria-hidden="true"></div>
    <p class="services">ff&amp;e furniture lighting textiles etc</p>
  </section>
</main>
</body>
</html>
```